Gift card design to reflect the theme from our overhead business sign

We need a gift card that aligns with our colors used for the sign. Since I am not sure what you're able to do with the limited space, if you think you can create a miniature version of the sign and add the words "Gift Card" to it. I'd like to see it. I have also uploaded the original logo we use as an other variable to use in place the horizontal one on the sign. That might be alright too. Give me a few options to consider.

Then for the back of the card there may be some legal requirements for the wording. I'll get back to you on that. First, let's focus on the design.

Also, i am sending the requirements for "Quorix" who will be the processor for the card. I will be doing custom cards so pay attention to page 4.

After the gift card, I will sending you the front of the store image with the sign in place, so you can come up with some ideas for a simple window design to go across all the windows.

How fast can you get back to me? Unlike the sign, I'm sort of in a time crunch.

Oh, one other thing, I want to change the pink in our current logo to the pink you used in the sign. So if you use our standard logo, please change the pink to the on you used for the sign.

```html
<!DOCTYPE html>
<html lang="en">
<head>
<meta charset="utf-8">
<title>Sugar Crate – Cards</title>
<link rel="stylesheet" href="https://fonts.googleapis.com/css2?family=Fredoka:wght@600&family=Montserrat:wght@400;500&display=swap">
<style>
  :root {
    --backdrop: #2c2c2e;
    --card-white: #ffffff;
    --coral: #f2827f;
    --coral-soft: #f7a8a5;
    --plum: #4b2a7b;
    --hot-pink: #e8298f;
    --hot-pink-light: #ee4a9f;
    --lime: #bad12f;
    --ink: #2a2a2a;
  }
  * { box-sizing: border-box; margin: 0; padding: 0; }
  html, body {
    width: 1200px; height: 1200px; overflow: hidden;
    background: var(--backdrop);
  }
  .stage {
    position: relative; width: 1200px; height: 1200px;
  }
  .card {
    position: absolute; left: 220px; width: 760px; height: 480px;
    border-radius: 34px; overflow: hidden;
  }
  /* Business card */
  .business-card { top: 90px; background: var(--card-white); }
  .business-card .brand {
    position: absolute; top: 120px; left: 0; right: 0;
    display: flex; justify-content: center; align-items: center; gap: 18px;
  }
  .brand-dot {
    width: 26px; height: 26px; border-radius: 50%; background: var(--plum);
  }
  .brand-name {
    font-family: "Fredoka", sans-serif; font-weight: 600;
    font-size: 86px; line-height: 1; color: var(--coral);
  }
  .contact-row {
    position: absolute; left: 48px; right: 48px; top: 300px;
    display: flex; justify-content: space-between; align-items: center;
    font-family: "Montserrat", sans-serif; font-size: 17px; color: var(--ink);
  }
  .contact-item { display: flex; align-items: center; gap: 8px; }
  .contact-item svg { width: 20px; height: 20px; flex: none; }
  .address { line-height: 1.2; }
  .stripe-band {
    position: absolute; left: 0; right: 0; bottom: 0; height: 92px;
    background: linear-gradient(90deg, var(--coral), var(--coral-soft), var(--coral));
  }
  /* Gift card */
  .gift-card {
    top: 620px;
    background: linear-gradient(120deg, var(--hot-pink) 0%, var(--hot-pink-light) 50%, var(--hot-pink) 100%);
  }
  .gift-card .brand {
    position: absolute; top: 92px; left: 0; right: 0;
    display: flex; flex-direction: column; align-items: center;
  }
  .gift-card .brand-name { color: #ffffff; font-size: 92px; }
  .tagline {
    margin-top: 6px;
    font-family: "Fredoka", sans-serif; font-weight: 600;
    font-size: 34px; color: #ffffff;
  }
  .gift-band {
    position: absolute; left: 0; right: 0; top: 300px; height: 76px;
    background: var(--lime);
    display: flex; align-items: center; justify-content: center;
  }
  .gift-label {
    font-family: "Fredoka", sans-serif; font-weight: 600;
    font-size: 46px; letter-spacing: 2px; color: #ffffff;
  }
</style>
</head>
<body>
<main class="stage">

  <section class="card business-card">
    <div class="brand">
      <span class="brand-dot"></span>
      <span class="brand-name">Sugar Crate</span>
    </div>

    <div class="contact-row">
      <div class="contact-item">
        <svg viewBox="0 0 24 24" aria-hidden="true"><path fill="var(--coral)" d="M6.6 10.8a15.1 15.1 0 0 0 6.6 6.6l2.2-2.2a1 1 0 0 1 1-.25 11.4 11.4 0 0 0 3.6.57 1 1 0 0 1 1 1V20a1 1 0 0 1-1 1A17 17 0 0 1 3 4a1 1 0 0 1 1-1h3.5a1 1 0 0 1 1 1c0 1.25.2 2.45.57 3.57a1 1 0 0 1-.25 1z"/></svg>
        <span>(000) 000 0000</span>
      </div>
      <div class="contact-item">
        <svg viewBox="0 0 24 24" aria-hidden="true"><rect x="2" y="5" width="20" height="14" rx="1.5" fill="var(--coral)"/><path d="M3 6l9 7 9-7" stroke="#fff" stroke-width="1.8" fill="none"/></svg>
        <span>email@company.com</span>
      </div>
      <div class="contact-item">
        <svg viewBox="0 0 24 24" aria-hidden="true"><path fill="var(--coral)" d="M12 2a7 7 0 0 0-7 7c0 5.2 7 13 7 13s7-7.8 7-13a7 7 0 0 0-7-7zm0 9.5A2.5 2.5 0 1 1 12 6.5a2.5 2.5 0 0 1 0 5z"/></svg>
        <span class="address">123 Name Street, 000<br>Your City, 00000-000</span>
      </div>
    </div>

    <div class="stripe-band" role="img" aria-label="Band of diagonal coral and white candy stripes"></div>
  </section>

  <section class="card gift-card">
    <div class="brand">
      <span class="brand-name">Sugar Crate</span>
      <span class="tagline">fresh bakes daily</span>
    </div>
    <div class="gift-band">
      <span class="gift-label">GIFT CARD</span>
    </div>
  </section>

</main>
</body>
</html>
```